Flyer
Zielgruppe
Ich bin Energieberater für Wohngebäude. Ich möchte ein Flyer über meine Leistungen erstellen. Dabei möchte ich gezielt potentielle Partner wie Architekten und Immobilienverwalter ansprechen und ein Netzwerk aufbauen.
Meine Leistungen im Überblick:
- Energieberatung
- Individueller Sanierungsfahrplan (iSFP)
- Energieausweise
- TbH-Effizienzhaus-Planung (Neubau und Bestand)
- Planung klimafreundlicher Neubau (KFN)
- Fördermittelberatung und -beantragung
- PUL-Einzelmaßnahmen wie z. B. Dämmung der Gebäudehülle oder Fenstertausch uvm.
- Heizlastberechnung nach DIN EN 12831
- Hydraulischer Abgleich nach Verfahren A/B
- Heizflächenauslegung
- Wärmepumpen (Beratung und Auslegung)
Meine Signatur:
M. Eng. Torben Wiskow
Energieberater / Planungsingenieur
Volmar Haus
Lindholzgasse 7C
47263 Gelsenkirchen
Tel: 0152 / 871 43 06
E-Mail: info@Volmar-Haus.de
Aufgabenstellung
Ich möchte den Flyer sowohl als PDF-Format nutzen, um Kalt-Akquise übers Internet zu betreiben, als auch ausgedruckt.

```html
<!DOCTYPE html>
<html lang="de">
<head>
<meta charset="utf-8">
<title>Volmar Haus – Flyer</title>
<link rel="stylesheet" href="https://fonts.googleapis.com/css2?family=Merriweather:ital,wght@0,400;0,700;0,900;1,400&display=swap">
<style>
  :root {
    --navy: #0d3560;
    --navy-deep: #06305a;
    --blue: #1a8fd4;
    --blue-bright: #1e95d8;
    --pale: #e1effb;
    --ink: #1d1d22;
    --white: #ffffff;
    --stage: #e4e5e7;
  }
  * { margin: 0; padding: 0; box-sizing: border-box; }
  html, body { width: 1200px; height: 1117px; overflow: hidden; background: var(--stage); }
  body { position: relative; font-family: "Merriweather", Georgia, serif; color: var(--ink); }

  .flyer {
    position: absolute; left: 226px; top: 30px;
    width: 748px; height: 1057px;
    background: var(--pale); overflow: hidden;
    box-shadow: 0 8px 24px rgba(0,0,0,.18);
  }
  .hero {
    position: absolute; left: 0; top: 0; width: 748px; height: 260px;
    background: linear-gradient(90deg, #eef0f3 0%, #dfe3e8 30%, #d3dcc2 48%, #f3f5f7 62%, #f7f9fb 70%, #cfe2f2 100%);
  }
  .hero-house {
    position: absolute; left: 470px; top: 40px; width: 278px; height: 380px;
    background: linear-gradient(180deg, #bfd9ee 0%, #e7eef2 40%, #c9c6b8 62%, #6e9ab8 80%, #3b79a6 100%);
  }
  .side-navy-left { position: absolute; left: 0; top: 520px; width: 62px; height: 240px; background: var(--navy-deep); }
  .side-navy-right { position: absolute; left: 688px; top: 790px; width: 60px; height: 210px; background: var(--navy-deep); }

  .content-panel {
    position: absolute; left: 62px; top: 232px; width: 628px; height: 600px;
    background: var(--white);
  }

  .brand {
    position: absolute; left: 400px; top: 240px;
    font-weight: 700; font-size: 20px; color: var(--navy); line-height: 1;
  }

  .headline {
    position: absolute; left: 78px; top: 284px; width: 640px;
    font-weight: 900; font-size: 37px; line-height: 1.12; color: var(--navy);
  }
  .headline .line-2 { display: block; padding-left: 52px; }
  .headline .accent { color: var(--blue); }

  .services-pill {
    position: absolute; left: 300px; top: 388px;
    background: var(--blue); color: var(--white);
    font-weight: 700; font-size: 18px; padding: 8px 22px; border-radius: 22px;
  }

  .service-list { position: absolute; list-style: none; font-size: 15.5px; line-height: 1.22; }
  .service-list li { position: relative; padding-left: 26px; margin-bottom: 4px; }
  .service-list li svg { position: absolute; left: 0; top: 3px; width: 16px; height: 12px; }
  .service-list.col-left { left: 84px; top: 446px; width: 300px; }
  .service-list.col-right { left: 392px; top: 500px; width: 290px; }

  .signature-label {
    position: absolute; left: 90px; top: 690px;
    font-weight: 700; font-size: 20px; color: var(--blue);
  }
  .signature-line { position: absolute; left: 110px; top: 752px; width: 200px; height: 2px; background: var(--blue); }
  .signature-name { position: absolute; left: 108px; top: 764px; font-weight: 700; font-size: 16px; }
  .signature-role { position: absolute; left: 108px; top: 788px; font-size: 11.5px; font-style: italic; }

  .footer-band { position: absolute; left: 0; top: 760px; width: 748px; height: 297px; }

  .contact { position: absolute; left: 68px; top: 880px; color: var(--white); font-style: normal; }
  .contact-row { position: relative; padding-left: 30px; margin-bottom: 6px; }
  .contact-row svg { position: absolute; left: 0; top: 4px; width: 18px; height: 18px; }
  .contact-company { font-weight: 700; font-size: 18px; }
  .contact-street { font-size: 14px; font-weight: 400; }
  .contact-phone, .contact-mail { font-weight: 700; font-size: 17px; }

  .portrait-ring {
    position: absolute; left: 368px; top: 770px; width: 290px; height: 290px;
    border-radius: 50%; background: var(--white); border: 5px solid var(--blue-bright);
    padding: 10px;
  }
  .portrait {
    width: 100%; height: 100%; border-radius: 50%;
    background: radial-gradient(circle at 50% 40%, #f3ece6 0%, #d6b49a 45%, #3a3430 85%);
  }
</style>
</head>
<body>
<main class="flyer">
  <div class="hero" role="img" aria-label="Foto: Energieeffizienzskala, Taschenrechner, Münzen und Hausmodell auf Bauplänen"></div>
  <div class="hero-house" role="img" aria-label="Foto: modernes Einfamilienhaus mit Pool"></div>

  <div class="side-navy-left"></div>
  <div class="side-navy-right"></div>

  <section class="content-panel"></section>

  <div class="brand">Volmar Haus</div>

  <h1 class="headline">Ingenieurtechnische Planung<span class="line-2">in der <span class="accent">Energiewende!</span></span></h1>

  <div class="services-pill">Meine Leistungen im Überblick:</div>

  <ul class="service-list col-left">
    <li><svg viewBox="0 0 16 12"><path d="M1 6l4 4 10-9" fill="none" stroke="#1a8fd4" stroke-width="3"/></svg>Energieberatung</li>
    <li><svg viewBox="0 0 16 12"><path d="M1 6l4 4 10-9" fill="none" stroke="#1a8fd4" stroke-width="3"/></svg>Individueller Sanierungsfahrplan (iSFP)</li>
    <li><svg viewBox="0 0 16 12"><path d="M1 6l4 4 10-9" fill="none" stroke="#1a8fd4" stroke-width="3"/></svg>Energieausweise</li>
    <li><svg viewBox="0 0 16 12"><path d="M1 6l4 4 10-9" fill="none" stroke="#1a8fd4" stroke-width="3"/></svg>TbH-Effizienzhaus-Planung (Neubau und Bestand)</li>
    <li><svg viewBox="0 0 16 12"><path d="M1 6l4 4 10-9" fill="none" stroke="#1a8fd4" stroke-width="3"/></svg>Planung klimafreundlicher Neubau (KFN)</li>
    <li><svg viewBox="0 0 16 12"><path d="M1 6l4 4 10-9" fill="none" stroke="#1a8fd4" stroke-width="3"/></svg>Fördermittelberatung und -beantragung</li>
  </ul>

  <ul class="service-list col-right">
    <li><svg viewBox="0 0 16 12"><path d="M1 6l4 4 10-9" fill="none" stroke="#1a8fd4" stroke-width="3"/></svg>PUL-Einzelmaßnahmen wie z. B. Dämmung der Gebäudehülle oder Fenstertausch uvm.</li>
    <li><svg viewBox="0 0 16 12"><path d="M1 6l4 4 10-9" fill="none" stroke="#1a8fd4" stroke-width="3"/></svg>Heizlastberechnung nach DIN EN 12831</li>
    <li><svg viewBox="0 0 16 12"><path d="M1 6l4 4 10-9" fill="none" stroke="#1a8fd4" stroke-width="3"/></svg>Hydraulischer Abgleich nach Verfahren A/B</li>
    <li><svg viewBox="0 0 16 12"><path d="M1 6l4 4 10-9" fill="none" stroke="#1a8fd4" stroke-width="3"/></svg>Heizflächenauslegung</li>
    <li><svg viewBox="0 0 16 12"><path d="M1 6l4 4 10-9" fill="none" stroke="#1a8fd4" stroke-width="3"/></svg>Wärmepumpen (Beratung und Auslegung)</li>
  </ul>

  <div class="signature-label">Meine Signatur:</div>
  <div class="signature-line"></div>
  <div class="signature-name">M. Eng. Torben Wiskow</div>
  <div class="signature-role">Energieberater / Planungsingenieur</div>

  <svg class="footer-band" viewBox="0 0 748 297" preserveAspectRatio="none" aria-hidden="true">
    <path d="M0 70 L330 140 L400 100 L748 190 L748 297 L0 297 Z" fill="#0d3560" opacity=".25"/>
    <path d="M0 60 L320 130 L360 110 C430 100 520 220 748 220 L748 297 L0 297 Z" fill="#1a8fd4"/>
  </svg>

  <address class="contact">
    <div class="contact-row contact-company">
      <svg viewBox="0 0 18 18"><path d="M9 1a6 6 0 0 0-6 6c0 4.5 6 10 6 10s6-5.5 6-10a6 6 0 0 0-6-6zm0 8.3A2.3 2.3 0 1 1 9 4.7a2.3 2.3 0 0 1 0 4.6z" fill="#fff"/></svg>
      Volmar Haus
      <div class="contact-street">Lindholzgasse 7C</div>
    </div>
    <div class="contact-row contact-phone">
      <svg viewBox="0 0 18 18"><circle cx="9" cy="9" r="8.5" fill="#fff"/><path d="M6 4.5l2 2-1 1.3c.6 1.3 1.5 2.2 2.8 2.8l1.3-1 2 2-1.3 1.5C8.5 13 5 9.5 4.5 5.8z" fill="#1a8fd4"/></svg>
      0152 / 871 43 06
    </div>
    <div class="contact-row contact-mail">
      <svg viewBox="0 0 18 18"><circle cx="9" cy="9" r="8.5" fill="#fff"/><rect x="4.5" y="6" width="9" height="6.5" fill="none" stroke="#1a8fd4" stroke-width="1.2"/><path d="M4.5 6l4.5 3.8L13.5 6" fill="none" stroke="#1a8fd4" stroke-width="1.2"/></svg>
      info@Volmar-Haus.de
    </div>
  </address>

  <div class="portrait-ring">
    <div class="portrait" role="img" aria-label="Porträtfoto des Energieberaters"></div>
  </div>
</main>
</body>
</html>
```